Data Collection Workbook

We are creating a data gathering booklet that will be completed by our clients (ages 40-90). Due to the volume of information being collected, we are looking for a format that is both inviting to complete and aesthetically pleasing to the eye. The final product will be approximately 20-30 pages, divided into 13 sections. A table of contents, as well as two sample pages are attached.

```html
<!DOCTYPE html>
<html lang="en">
<head>
<meta charset="utf-8">
<title>Financial Obligation</title>
<link rel="stylesheet" href="https://fonts.googleapis.com/css2?family=Noto+Sans:wght@400;700&display=swap">
<style>
  :root {
    --mint: #66ffcc;
    --mint-pale: #ddfff3;
    --mint-line: #7ff5d0;
    --violet: #cc66ff;
    --ink: #000000;
    --paper: #ffffff;
  }
  * { box-sizing: border-box; margin: 0; padding: 0; }
  html, body { width: 849px; height: 1200px; overflow: hidden; background: var(--paper); }
  body { font-family: "Noto Sans", Verdana, sans-serif; color: var(--ink); }
  .page { position: relative; width: 849px; height: 1200px; border: 1px solid #333; overflow: hidden; }
  .top-band { position: absolute; left: 0; top: 0; width: 799px; height: 62px; background: var(--mint); }
  .title-rule { position: absolute; left: 0; top: 134px; width: 799px; height: 12px; background: var(--mint); }
  .corner-tab { position: absolute; left: 799px; top: 0; width: 50px; height: 146px; background: var(--violet); }
  .page-title { position: absolute; left: 95px; top: 62px; font-size: 54px; font-weight: 700; color: var(--violet); line-height: 72px; letter-spacing: 0.3px; }
  .section-heading { position: absolute; left: 82px; font-size: 20px; font-weight: 700; line-height: 24px; }
  .entry-list { position: absolute; left: 82px; width: 739px; list-style: none; }
  .entry { position: relative; height: 44.9px; border-left: 2px solid var(--mint-line); border-bottom: 2px solid var(--mint-line); }
  .entry-labels { display: flex; height: 15px; background: var(--mint-pale); font-size: 11.5px; font-weight: 700; line-height: 15px; }
  .entry-labels span { position: absolute; top: 0; white-space: nowrap; }
  .lbl-name { left: 8px; }
  .lbl-account { left: 208px; }
  .lbl-login { left: 318px; }
  .lbl-paid { left: 511px; }
  .lbl-paid em { font-style: normal; font-weight: 400; }
  .page-number { position: absolute; left: 733px; top: 1084px; width: 80px; height: 80px; background: var(--violet); border-radius: 40px 40px 0 40px; color: var(--paper); font-size: 30px; text-align: center; line-height: 80px; }
</style>
</head>
<body>
<div class="page">
  <div class="top-band"></div>
  <div class="title-rule"></div>
  <div class="corner-tab"></div>
  <h1 class="page-title">Financial Obligation</h1>

  <h2 class="section-heading" style="top:191px">General liabilities (Attach 1st page of statement for each account):</h2>
  <ul class="entry-list" style="top:224px">
    <li class="entry"><div class="entry-labels"><span class="lbl-name">Mortgage Lender 1</span><span class="lbl-account">Account #</span><span class="lbl-login">Website Username/Password</span><span class="lbl-paid">How Paid? <em>(online, check, billpay etc)</em></span></div></li>
    <li class="entry"><div class="entry-labels"><span class="lbl-name">Mortgage Lender 2</span><span class="lbl-account">Account #</span><span class="lbl-login">Website Username/Password</span><span class="lbl-paid">How Paid? <em>(online, check, billpay etc)</em></span></div></li>
    <li class="entry"><div class="entry-labels"><span class="lbl-name">Mortgage Lender 3</span><span class="lbl-account">Account #</span><span class="lbl-login">Website Username/Password</span><span class="lbl-paid">How Paid? <em>(online, check, billpay etc)</em></span></div></li>
    <li class="entry"><div class="entry-labels"><span class="lbl-name">Home Equity Line</span><span class="lbl-account">Account #</span><span class="lbl-login">Website Username/Password</span><span class="lbl-paid">How Paid? <em>(online, check, billpay etc)</em></span></div></li>
    <li class="entry"><div class="entry-labels"><span class="lbl-name">Auto 1</span><span class="lbl-account">Account #</span><span class="lbl-login">Website Username/Password</span><span class="lbl-paid">How Paid? <em>(online, check, billpay etc)</em></span></div></li>
    <li class="entry"><div class="entry-labels"><span class="lbl-name">Auto 2</span><span class="lbl-account">Account #</span><span class="lbl-login">Website Username/Password</span><span class="lbl-paid">How Paid? <em>(online, check, billpay etc)</em></span></div></li>
    <li class="entry"><div class="entry-labels"><span class="lbl-name">Personal Debt</span><span class="lbl-account">Account #</span><span class="lbl-login">Website Username/Password</span><span class="lbl-paid">How Paid? <em>(online, check, billpay etc)</em></span></div></li>
    <li class="entry"><div class="entry-labels"><span class="lbl-name">Line of Credit</span><span class="lbl-account">Account #</span><span class="lbl-login">Website Username/Password</span><span class="lbl-paid">How Paid? <em>(online, check, billpay etc)</em></span></div></li>
    <li class="entry"><div class="entry-labels"><span class="lbl-name">Other</span><span class="lbl-account">Account #</span><span class="lbl-login">Website Username/Password</span><span class="lbl-paid">How Paid? <em>(online, check, billpay etc)</em></span></div></li>
  </ul>

  <h2 class="section-heading" style="top:651px">Credit Cards (Attach 1st page of statement for each account):</h2>
  <ul class="entry-list" style="top:684px">
    <li class="entry"><div class="entry-labels"><span class="lbl-name">Credit Card Company 1</span><span class="lbl-account">Account #</span><span class="lbl-login">Website Username/Password</span><span class="lbl-paid">How Paid? <em>(online, check, billpay etc)</em></span></div></li>
    <li class="entry"><div class="entry-labels"><span class="lbl-name">Credit Card Company 2</span><span class="lbl-account">Account #</span><span class="lbl-login">Website Username/Password</span><span class="lbl-paid">How Paid? <em>(online, check, billpay etc)</em></span></div></li>
    <li class="entry"><div class="entry-labels"><span class="lbl-name">Credit Card Company 3</span><span class="lbl-account">Account #</span><span class="lbl-login">Website Username/Password</span><span class="lbl-paid">How Paid? <em>(online, check, billpay etc)</em></span></div></li>
    <li class="entry"><div class="entry-labels"><span class="lbl-name">Credit Card Company 4</span><span class="lbl-account">Account #</span><span class="lbl-login">Website Username/Password</span><span class="lbl-paid">How Paid? <em>(online, check, billpay etc)</em></span></div></li>
    <li class="entry"><div class="entry-labels"><span class="lbl-name">Credit Card Company 5</span><span class="lbl-account">Account #</span><span class="lbl-login">Website Username/Password</span><span class="lbl-paid">How Paid? <em>(online, check, billpay etc)</em></span></div></li>
    <li class="entry"><div class="entry-labels"><span class="lbl-name">Credit Card Company 6</span><span class="lbl-account">Account #</span><span class="lbl-login">Website Username/Password</span><span class="lbl-paid">How Paid? <em>(online, check, billpay etc)</em></span></div></li>
    <li class="entry"><div class="entry-labels"><span class="lbl-name">Credit Card Company 7</span><span class="lbl-account">Account #</span><span class="lbl-login">Website Username/Password</span><span class="lbl-paid">How Paid? <em>(online, check, billpay etc)</em></span></div></li>
    <li class="entry"><div class="entry-labels"><span class="lbl-name">Credit Card Company 8</span><span class="lbl-account">Account #</span><span class="lbl-login">Website Username/Password</span><span class="lbl-paid">How Paid? <em>(online, check, billpay etc)</em></span></div></li>
    <li class="entry"></li>
  </ul>

  <div class="page-number">9</div>
</div>
</body>
</html>
```